Find Bright Harbor Business Card and logo

We need a logo design and business card for a new consulting firm called Find Bright Harbor. We specialize in Digital Transformation of enterprises of all sizes. We help enterprises understand & significantly increase their business velocity. This requires changes in culture, organization, process and technology. We also partner with advanced technology companies to deliver tangible accelerated solutions. Methods utilized include Agile, Design Thinking, Advanced Technology Platforms (microservices, digital data, virtualization, blockchain, etc.). The final design should communicate velocity, transformation, growth and innovation.

Target Market(s)

Large Corporations and Enterprises

Contact Information for Business Card

Tagline - Shape the Coming

Logo Text

Find Bright Harbor or an initial or initials or a symbol/picture

Requirements
Must have
• Front side: Logo, name of business (Find Bright Harbor), tagline (Shape the Coming)
• Back side: First Name, Last Name, Title, Mobile Phone, Email, LinkedIn, URL (findbrightharbor.com)
Nice to have
• The design should communicate velocity, transformation, growth and/or innovation.

```html
<!DOCTYPE html>
<html lang="en">
<head>
<meta charset="utf-8">
<title>Find Bright Harbor – Business Card</title>
<link rel="stylesheet" href="https://fonts.googleapis.com/css2?family=Kumbh+Sans:wght@700&family=Lato:wght@400&family=Montserrat:wght@500&display=swap">
<style>
  :root {
    --backdrop: #c6c6c6;
    --card-light: #fbfbfb;
    --card-dark: #2b2b2b;
    --ink: #111111;
    --ink-soft: #222222;
    --white: #ffffff;
    --muted: #a8a8a8;
    --accent: #f0421c;
    --accent-faint: #f7cfc8;
    --icon-red: #e3231b;
    --icon-blue: #1a7bc0;
  }
  * { margin: 0; padding: 0; box-sizing: border-box; }
  html, body { width: 1200px; height: 1200px; overflow: hidden; }
  body { background: var(--backdrop); position: relative; font-family: "Lato", sans-serif; }

  .card {
    position: absolute;
    width: 368px;
    height: 592px;
    border-radius: 18px;
    overflow: hidden;
  }
  .card--back { left: 232px; top: 311px; background: var(--card-light); }
  .card--front { left: 628px; top: 312px; background: var(--card-dark); }

  .brand-name {
    position: absolute;
    left: 0; right: 0;
    text-align: center;
    font-family: "Kumbh Sans", sans-serif;
    font-weight: 700;
    font-size: 31px;
    letter-spacing: -0.2px;
  }
  .tagline {
    position: absolute;
    left: 0; right: 0;
    display: flex;
    align-items: center;
    justify-content: center;
    gap: 12px;
    font-family: "Montserrat", sans-serif;
    font-weight: 500;
    font-size: 12px;
    letter-spacing: 2.6px;
    text-transform: uppercase;
  }
  .tagline::before, .tagline::after {
    content: "";
    width: 48px;
    height: 1px;
    background: currentColor;
  }

  .card--back .brand-name { top: 125px; color: var(--ink); }
  .card--back .tagline { top: 164px; color: var(--ink); }

  .faint-ring {
    position: absolute;
    left: 100px; top: 306px;
    width: 260px; height: 260px;
    border-radius: 50%;
    border: 17px solid var(--accent-faint);
    opacity: 0.85;
  }

  .person { position: absolute; left: 36px; top: 362px; color: var(--ink-soft); }
  .person__name {
    font-family: "Kumbh Sans", sans-serif;
    font-weight: 700;
    font-size: 25px;
    color: var(--ink);
    line-height: 1.1;
  }
  .person__title { font-size: 17px; margin-top: 1px; }

  .contact-list { position: absolute; left: 36px; top: 428px; list-style: none; }
  .contact-list li {
    display: flex;
    align-items: center;
    gap: 6px;
    font-size: 16.5px;
    line-height: 21.7px;
    color: var(--ink-soft);
  }
  .contact-list svg { width: 14px; height: 14px; flex: none; }

  .card--front .mark-ring {
    position: absolute;
    left: 114px; top: 196px;
    width: 140px; height: 140px;
    border-radius: 50%;
    border: 9px solid var(--accent);
  }
  .card--front .brand-name { top: 346px; color: var(--white); }
  .card--front .tagline { top: 386px; color: var(--muted); }
</style>
</head>
<body>

<section class="card card--back">
  <h1 class="brand-name">Find Bright Harbor</h1>
  <p class="tagline">Shape the Coming</p>

  <div class="faint-ring" aria-hidden="true"></div>

  <div class="person">
    <p class="person__name">Marcus Ellery</p>
    <p class="person__title">Managing Director</p>
  </div>

  <ul class="contact-list">
    <li>
      <svg viewBox="0 0 14 14" aria-hidden="true"><path fill="var(--icon-red)" d="M1 5c0-2 2-3 6-3s6 1 6 3v1h-3V4.5H4V6H1zM3 7h8l1 5H2z"/><circle cx="7" cy="9.3" r="1.4" fill="#fff"/></svg>
      <span>044-555 019 372</span>
    </li>
    <li>
      <svg viewBox="0 0 14 14" aria-hidden="true"><rect x="1" y="3" width="12" height="8.5" fill="var(--icon-red)"/><path d="M1.5 3.5 7 8l5.5-4.5" fill="none" stroke="#fff" stroke-width="1.2"/></svg>
      <span>hello@findbrightharbor.com</span>
    </li>
    <li>
      <svg viewBox="0 0 14 14" aria-hidden="true"><circle cx="7" cy="7" r="6" fill="var(--icon-red)"/><path d="M4 4.5c1.5 0 2 1 2.8 1.8-.6 1-1.8.8-2 2.2M9 9.5c.4-1 1.4-1 2-2" fill="none" stroke="#fff" stroke-width="1.3"/></svg>
      <span>www.findbrightharbor.com</span>
    </li>
    <li>
      <svg viewBox="0 0 14 14" aria-hidden="true"><circle cx="7" cy="7" r="6.5" fill="var(--icon-blue)"/></svg>
      <span>MarcusEllery</span>
    </li>
  </ul>
</section>

<section class="card card--front">
  <div class="mark-ring" aria-hidden="true"></div>
  <h2 class="brand-name">Find Bright Harbor</h2>
  <p class="tagline">Shape the Coming</p>
</section>

</body>
</html>
```